Flyer-Design für Immobilienfirma
Zielgruppe
www.brenkholt-immobilien.de
Aufgabenstellung
Thema :
Neukunden generieren – Viele Wege führen zu neuen Leads ...
Sich selbst als Experten platzieren mit Bild
Dienstleistung : FÜR DEN IMMOBILIENBESITZER
Was ist Ihre Immobilie wert?
KOSTENLOSE Beratung durch Experten
KOSTENLOSE Immobilienbewertung
KOSTENLOS vorhandene Grundrisszeichnungen aktualisieren
KOSTENLOS 3D Grundrisszeichnungen und Ansicht
KOSTENLOS 3D Fotos und 360 Grad Ansichten
KOSTENLOS Drohnenaufnahmen IHRER Immobilien
KOSTENLOS Erstellung eines Energieverbrauchsausweises
evtl für die Rückseite
#Tippgeberprämie
Brenkholt & Partner Immobilien
so einfach verdienen Sie sich Ihre Tippprämie
wenn Sie Kenntnis vom beabsichtigten Verkauf einer Immobilie haben, dann setzen Sie sich mit uns in Verbindung.
Wir belohnen Ihren Tipp – wenn er zu einem Verkaufsabschluss durch uns führt –
mit 10 Prozent der an uns gezahlten Netto-Vermittlungsprovision (ohne MwSt.).
Dies gilt auch für Eigentümer, die uns Ihre Immobilie zum Verkauf geben.
Voraussetzungen für die Zahlung einer Tippgeber-Prämie sind:
Die Brenkholt & Partner immobilien kennt das angebotene Objekt noch nicht.
Das Objekt wird nicht bereits im Internet von dritter Seite beworben.
Die Brenkholt & Partner immobilien erhält die Erlaubnis zur Vermarktung der Immobilie.
Es kommt zu einem durch die Brenkholt & Partner immobilien vermittelten Verkauf
Sie erhalten Ihre Tippprämie unmittelbar nach Zahlung der Courtage an uns auf ein von Ihnen genanntes Konto überwiesen!

```html
<!DOCTYPE html>
<html lang="de">
<head>
<meta charset="utf-8">
<title>Brenkholt &amp; Partner – Flyer</title>
<link rel="stylesheet" href="https://fonts.googleapis.com/css2?family=Jost:wght@300;400;500&display=swap">
<style>
  :root {
    --gold: #d9ae52;
    --text: #5a5a5a;
    --brand: #4a3b2a;
    --paper: #ffffff;
    --backdrop: #e4e4e4;
    --sky: #8cc4e6;
    --facade: #e9ecef;
    --lawn: #7fa45a;
  }
  * { margin: 0; padding: 0; box-sizing: border-box; }
  html, body { width: 1200px; height: 1200px; overflow: hidden; }
  body {
    background: var(--backdrop);
    font-family: "Jost", Arial, sans-serif;
    color: var(--text);
  }
  .flyer {
    position: absolute;
    left: 177px; top: 0;
    width: 846px; height: 1200px;
    background: var(--paper);
  }
  .brand {
    position: absolute;
    left: 580px; top: 70px;
    display: flex; align-items: center; gap: 10px;
    color: var(--brand);
    font-weight: 500;
  }
  .brand-dot { width: 14px; height: 14px; border-radius: 50%; background: var(--brand); }
  .brand-name { font-size: 24px; line-height: 1; }
  .brand-sub { font-size: 11px; line-height: 1.4; }
  .headline {
    position: absolute;
    left: 29px; top: 198px; width: 790px;
    font-weight: 300;
    font-size: 35.5px;
    letter-spacing: 0.2px;
    white-space: nowrap;
    color: var(--text);
  }
  .accent-bar {
    position: absolute; left: 0; top: 274px;
    width: 28px; height: 383px; background: var(--gold);
  }
  .photo { position: absolute; top: 274px; height: 383px; }
  .photo-townhouse {
    left: 28px; width: 354px;
    background: linear-gradient(180deg, var(--sky) 0%, #c7e2f2 30%, var(--facade) 45%, #6c7580 70%, var(--lawn) 95%);
  }
  .photo-villa {
    left: 399px; width: 447px;
    background: linear-gradient(180deg, #86a8cf 0%, #c9d8e6 30%, #f1f1f1 55%, #cfcfcf 78%, #6f9a4e 100%);
  }
  .portrait {
    position: absolute;
    left: 174px; top: 679px;
    width: 192px; height: 192px; border-radius: 50%;
    background: radial-gradient(circle at 50% 45%, #d9c3a8 0%, #a98a6c 45%, #2c3850 100%);
  }
  .question {
    position: absolute;
    right: 501px; top: 883px;
    text-align: right;
    font-weight: 300; font-size: 23px; line-height: 30px;
  }
  .benefits {
    position: absolute;
    left: 399px; top: 708px; width: 430px;
    list-style: none;
    border-top: 1px solid var(--gold);
  }
  .benefits li {
    height: 59.7px;
    border-bottom: 1px solid var(--gold);
    padding-top: 5px;
    font-weight: 300; font-size: 18px; line-height: 24px;
    white-space: nowrap;
  }
  .benefits .label { display: block; text-transform: uppercase; }
  .contact-band {
    position: absolute;
    left: 28px; top: 1113px;
    width: 818px; height: 85px;
    background: var(--gold);
    color: #fff;
    font-weight: 300;
  }
  .contact-web {
    position: absolute; left: 58px; top: 17px;
    font-size: 16.5px; line-height: 22px;
  }
  .contact-phone {
    position: absolute; left: 373px; top: 20px;
    font-size: 29px; line-height: 40px;
  }
</style>
</head>
<body>
  <main class="flyer">
    <div class="brand">
      <span class="brand-dot"></span>
      <div>
        <div class="brand-name">Brenkholt</div>
        <div class="brand-sub">&amp; Partner Real Estate</div>
      </div>
    </div>

    <h1 class="headline">IHRE IMMOBILIE BESTMÖGLICHST VERKAUFEN</h1>

    <div class="accent-bar"></div>
    <div class="photo photo-townhouse" role="img" aria-label="Foto: modernes weißes Stadthaus mit dunkler Fassade vor blauem Himmel"></div>
    <div class="photo photo-villa" role="img" aria-label="Foto: weiße Bauhaus-Villa mit Holz-Garagentor und Garten"></div>

    <div class="portrait" role="img" aria-label="Porträtfoto des Immobilienexperten"></div>
    <p class="question">Was ist Ihre Immobilie<br>wirklich wert?</p>

    <ul class="benefits">
      <li><span class="label">Kostenlose</span>Beratung durch Experten</li>
      <li><span class="label">Kostenlose</span>Immobilienbewertung</li>
      <li><span class="label">Kostenlos</span>vorhandene Grundrisszeichnungen aktualisieren</li>
      <li><span class="label">Kostenlos</span>3D Grundrisszeichnungen und Ansicht</li>
      <li><span class="label">Kostenlos</span>3D Fotos und 360 Grad Ansichten</li>
      <li><span class="label">Kostenlos</span>Drohnenaufnahmen IHRER Immobilien</li>
    </ul>

    <footer class="contact-band">
      <div class="contact-web">www.brenkholt-immobilien.de<br>kontakt@brenkholt-immobilien.de</div>
      <div class="contact-phone">+49 (0) 421 55 60 31 42-70</div>
    </footer>
  </main>
</body>
</html>
```